Post storm repair flyer

looking for an eye catching 6x9 postcard to send out to single family home owners advertising a "Post Storm Repair Special" explaining that after the recent hurricanes its very important to have your roof checked and any repairs fixed right away before they become a bigger more costly problem and that even though your home wasn't directly hit by the storm the high wind gust could've cause unseen damage.
offer $200 off any repair *some rules may apply
Lark Roofing
888.417.LARK
www.LarkRoofing.example

Roofing

```html
<!DOCTYPE html>
<html lang="en">
<head>
<meta charset="utf-8">
<title>Lark Roofing – Post Storm Repair Special Postcard</title>
<link rel="stylesheet" href="https://fonts.googleapis.com/css2?family=Bebas+Neue&family=Oswald:wght@500;600&family=Montserrat:wght@300;400;500;600;700&display=swap">
<style>
:root{
  --backdrop:#fbb94f;
  --panel:#1b1b1b;
  --gold:#f5b818;
  --white:#ffffff;
  --rule:#a7a7a9;
  --sky-top:#e3ecf3;
  --sky-bottom:#9aa0a6;
}
*{margin:0;padding:0;box-sizing:border-box}
html,body{width:901px;height:1200px;overflow:hidden;background:var(--backdrop)}
.postcard{position:absolute;left:62px;width:776px;height:518px;overflow:hidden;box-shadow:0 6px 14px rgba(0,0,0,.25);font-family:"Montserrat",sans-serif;color:var(--white)}
.postcard--front{top:72px;background:var(--white)}
.postcard--back{top:611px;background:var(--white)}
.card-shapes{position:absolute;inset:0}
.brand-name{position:absolute;left:0;width:234px;text-align:center;font-family:"Montserrat",sans-serif;font-weight:700;font-size:23px;letter-spacing:.2px;line-height:1}
.headline{position:absolute;left:27px;top:155px;font-family:"Bebas Neue",sans-serif;font-weight:400;font-size:57px;line-height:46px;text-transform:uppercase;letter-spacing:-.2px}
.headline .accent{color:var(--gold);display:block}
.damage-samples{position:absolute;left:26px;top:260px;display:flex;gap:3px}
.damage-sample{width:96px;height:60px;border:1.5px solid var(--white);border-radius:6px}
.damage-sample--1{background:linear-gradient(135deg,#8d939b,#b6bcc3 55%,#6c727a)}
.damage-sample--2{background:linear-gradient(160deg,#d5d8dc 0 30%,#4a4d52 30%,#2e3034)}
.damage-sample--3{background:linear-gradient(135deg,#3a3c40 0 45%,#9ea3a8 45%,#c7c9cb)}
.gold-rule{position:absolute;height:2px;background:var(--gold)}
.intro-copy{position:absolute;left:27px;top:341px;width:348px;font-size:13px;line-height:17px;font-weight:500;letter-spacing:.25px}
.offer{position:absolute;left:27px;color:var(--gold);line-height:1}
.offer-amount{font-family:"Oswald",sans-serif;font-weight:600;text-transform:uppercase}
.offer-terms{font-family:"Montserrat",sans-serif;font-weight:400;color:var(--white)}
.contact{position:absolute;left:27px}
.contact-name{font-weight:400;text-transform:uppercase;line-height:1}
.contact-phone{font-family:"Oswald",sans-serif;font-weight:600;color:var(--gold);line-height:1}
.contact-web{font-weight:300;line-height:1}
.back-message{position:absolute;left:27px;top:198px;width:335px;font-size:24.5px;line-height:28.7px;font-weight:500}
.stamp-box{position:absolute;left:626px;top:36px;width:122px;height:122px;border:2px solid var(--rule)}
.address-line{position:absolute;left:531px;width:218px;height:2px;background:var(--rule)}
.faint-brand{position:absolute;left:640px;top:455px;width:120px;text-align:center;font-weight:600;font-size:14px;color:#e4e4e6}
</style>
</head>
<body>

<section class="postcard postcard--front" aria-label="Postcard front">
  <svg class="card-shapes" viewBox="0 0 776 518" width="776" height="518">
    <defs>
      <linearGradient id="roofPhoto" x1="0" y1="0" x2="0" y2="1">
        <stop offset="0" stop-color="var(--sky-top)"/>
        <stop offset=".55" stop-color="#c9cfd5"/>
        <stop offset="1" stop-color="var(--sky-bottom)"/>
      </linearGradient>
    </defs>
    <rect x="220" y="0" width="556" height="518" fill="url(#roofPhoto)" role="img" aria-label="Photo of two roofers in hard hats and safety vests repairing a tiled roof"/>
    <polygon points="0,0 243,0 536,518 0,518" fill="var(--panel)"/>
    <polygon points="243,0 266,0 467,365 450,365" fill="var(--gold)"/>
  </svg>

  <div class="brand-name" style="top:104px">LARK ROOFING</div>

  <h1 class="headline">
    <span class="accent">Post Storm</span>
    Repair Special
  </h1>

  <div class="damage-samples" role="img" aria-label="Three photos of storm-damaged roof shingles and a house gable">
    <div class="damage-sample damage-sample--1"></div>
    <div class="damage-sample damage-sample--2"></div>
    <div class="damage-sample damage-sample--3"></div>
  </div>

  <div class="gold-rule" style="left:27px;top:333px;width:174px"></div>

  <p class="intro-copy">After the recent hurricanes, it's very important to have your roof checked and any repairs fixed right away before they become a bigger, more costly problem.</p>

  <div class="offer" style="top:412px">
    <span class="offer-amount" style="font-size:13px">$200 off any repair*</span>
    <span class="offer-terms" style="font-size:9px">&nbsp;*some rules may apply</span>
  </div>

  <div class="contact" style="top:432px">
    <div class="contact-name" style="font-size:20px">Lark Roofing</div>
    <div class="contact-phone" style="font-size:30px;margin-top:1px">888.417.LARK</div>
    <div class="contact-web" style="font-size:16px;margin-top:2px">www.LarkRoofing.example</div>
  </div>
</section>

<section class="postcard postcard--back" aria-label="Postcard back">
  <svg class="card-shapes" viewBox="0 0 776 518" width="776" height="518">
    <defs>
      <linearGradient id="panelPhoto" x1="0" y1="0" x2="0" y2="1">
        <stop offset="0" stop-color="#1b1b1b"/>
        <stop offset=".5" stop-color="#2a2a29"/>
        <stop offset="1" stop-color="#222222"/>
      </linearGradient>
    </defs>
    <polygon points="0,0 241,0 538,518 0,518" fill="url(#panelPhoto)" role="img" aria-label="Darkened photo of roofers working on a roof behind the text"/>
    <polygon points="336,142 350,142 552,518 538,518" fill="var(--gold)"/>
  </svg>

  <div class="brand-name" style="top:109px">LARK ROOFING</div>

  <p class="back-message">Even though your home wasn't directly hit by the storm, the highest wind gust could've caused unseen damage.</p>

  <div class="gold-rule" style="left:27px;top:353px;width:216px"></div>

  <div class="offer" style="top:364px">
    <div class="offer-amount" style="font-size:20px">$200 off any repair*</div>
    <div class="offer-terms" style="font-size:10px;margin-top:3px">*some rules may apply</div>
  </div>

  <div class="contact" style="top:404px">
    <div class="contact-name" style="font-size:25px">Lark Roofing</div>
    <div class="contact-phone" style="font-size:37px;margin-top:1px">888.417.LARK</div>
    <div class="contact-web" style="font-size:19px;margin-top:3px">www.LarkRoofing.example</div>
  </div>

  <div class="stamp-box" aria-hidden="true"></div>
  <div class="address-line" style="top:208px"></div>
  <div class="address-line" style="top:254px"></div>
  <div class="address-line" style="top:301px"></div>

  <div class="faint-brand">LARK ROOFING</div>
</section>

</body>
</html>
```